Law Firm Business Card

This is a business card for a law firm that serves US military and veterans.

The card must have ONLY the following (we want an uncluttered look):

- Company logo (PNG, GIF, JPEG copies uploaded)
- A tagline reading: "a law firm for service members and veterans"
- My name and title: "Martin Kovel" and "Attorney"
- My email: "mart.kovel@bramblecourtlegal.com"
- My number: "855-MOKE-TIB (665-3842)"

We are looking for a clean, simple layout with only the above information, likely printed on a bright white cotton stock. The font of our logo is DIN 1451, and the font used on our website is Helvetica Neue. The color of our logo is #336699, and we probably want the tagline in that color also, and my contact information in a dark grey. Please review our website at www.bramblecourtlegal.com to ensure your card design complements our website style.

Thanks and we look forward to seeing your submissions.

A few notes:

- Two-sided submissions are ok
- Please don't add graphics (scales of justice, judges hammer, etc)

```html
<!DOCTYPE html>
<html lang="en">
<head>
<meta charset="utf-8">
<title>Bramble Court Legal – Business Card</title>
<link rel="stylesheet" href="https://fonts.googleapis.com/css2?family=Lexend:wght@400&family=Roboto+Condensed:wght@400&family=Lato:wght@400;700&display=swap">
<style>
  :root {
    --page: #ffffff;
    --card: #c1cac8;
    --brand-blue: #2f61bf;
    --rule-blue: #3566c4;
    --ink-light: #ffffff;
    --brush-grey: #9aa3a2;
  }
  html, body {
    margin: 0;
    padding: 0;
    width: 1200px;
    height: 700px;
    overflow: hidden;
    background: var(--page);
  }
  .canvas {
    position: relative;
    width: 1200px;
    height: 700px;
  }
  .card {
    position: absolute;
    left: 38px;
    top: 38px;
    width: 1135px;
    height: 629px;
    background: var(--card);
  }
  .divider {
    position: absolute;
    left: 575px;
    top: 53px;
    width: 3px;
    height: 520px;
    background: var(--rule-blue);
  }
  .firm-name {
    position: absolute;
    left: 30px;
    top: 340px;
    width: 500px;
    margin: 0;
    color: var(--brand-blue);
    font-family: "Lato", "Helvetica Neue", sans-serif;
    font-weight: 700;
    font-size: 46px;
    line-height: 1;
    text-align: center;
    white-space: nowrap;
  }
  .tagline {
    position: absolute;
    left: 39px;
    top: 530px;
    width: 505px;
    margin: 0;
    color: var(--ink-light);
    font-family: "Lato", "Helvetica Neue", sans-serif;
    font-size: 16px;
    letter-spacing: 2.6px;
    word-spacing: 4px;
    white-space: nowrap;
  }
  .name-brush {
    position: absolute;
    left: 653px;
    top: 100px;
    width: 397px;
    height: 110px;
  }
  .person {
    position: absolute;
    left: 660px;
    top: 103px;
    width: 420px;
    margin: 0;
    color: var(--ink-light);
    font-family: "Lexend", "Helvetica Neue", sans-serif;
    font-weight: 400;
    text-align: center;
    font-size: 38px;
    letter-spacing: 4px;
    line-height: 52px;
  }
  .person__name,
  .person__title {
    display: block;
  }
  .person__title {
    padding-left: 30px;
  }
  .name-rule {
    position: absolute;
    left: 722px;
    top: 279px;
    width: 294px;
    height: 2px;
    background: var(--rule-blue);
  }
  .contact {
    position: absolute;
    left: 635px;
    top: 404px;
    margin: 0;
    font-family: "Roboto Condensed", "Arial Narrow", sans-serif;
    font-size: 23px;
    color: var(--ink-light);
  }
  .contact__row {
    display: flex;
    align-items: baseline;
    height: 40px;
  }
  .contact__label {
    color: var(--brand-blue);
    font-family: "Lato", "Helvetica Neue", sans-serif;
    font-weight: 700;
    font-size: 22px;
    letter-spacing: 1px;
  }
  .contact__label--email {
    width: 58px;
    padding-left: 4px;
    font-size: 20px;
  }
  .contact__label--phone {
    width: 56px;
  }
  .contact__value--phone {
    font-family: "Lexend", "Helvetica Neue", sans-serif;
    font-size: 21px;
    letter-spacing: 2.6px;
  }
</style>
</head>
<body>
<div class="canvas">
  <div class="card">
    <h1 class="firm-name">Bramble Court Legal</h1>
    <p class="tagline">a law firm for service members and veterans</p>

    <div class="divider"></div>

    <svg class="name-brush" viewBox="0 0 397 110" role="img" aria-label="Grey brush-stroke accent behind the name">
      <polygon points="22,8 392,2 374,58 302,64 307,100 10,108 26,62 0,56" fill="var(--brush-grey)"/>
    </svg>
    <h2 class="person">
      <span class="person__name">Martin Kovel</span>
      <span class="person__title">Attorney</span>
    </h2>
    <div class="name-rule"></div>

    <div class="contact">
      <div class="contact__row">
        <span class="contact__label contact__label--email">@:</span>
        <span class="contact__value">mart.kovel@bramblecourtlegal.com</span>
      </div>
      <div class="contact__row">
        <span class="contact__label contact__label--phone">Ph:</span>
        <span class="contact__value contact__value--phone">855-MOKE-TIB (665-3842)</span>
      </div>
    </div>
  </div>
</div>
</body>
</html>
```